Harwick Physiotherapy needs a brochure that will highlight and sell our services to prospective clie

Harwick Physiotherapy. The treatment you need , the care you deserve.

We need a brochure design for our musculoskeletal physiotherapy business. It needs to sell our service to prospective clients and to referrers and communicate our values and mission. It needs to incorporate our services of: back and neck pain, muscle and joint sprains and strains, sports injury management, including video assessment, acupuncture, Pilates, women's health/pelvic floor physio, deep tissue massage. We use technology including video analysis to improve patient outcomes. Our website is http://harwickphysio.co.nz attached are some images from web site and some graphics including our logo

Ideally a front page with our logo and graphics and bulletin points of our services

Sports Injuries
Back , neck and joint pain
Orthopedic rehabilitation
Acupuncture
Pelvic floor Physiotherapy

Then inside our USP's why us (see our web site) plus ....
We provide expert diagnosis of your problem and committed/dedicated to providing the best possible solution to get you back to what you love and improve your performance
Also we specialise in the use of technology with video analysis (http://www.strivelens.com/), digital postural analysis software (http://alignmetrix.com/mobile/), computer graphics for education (http://applications.anatovista.com/shoulder_pro) and video/online exercise programs (https://www.kinetrova.org/index.php), online booking (http://nzappts.bookrally.com/harwick/)
Long appointments , not rushed , to give us time to help

Then sections for:

Physiotherapy
sports physio
Orthopaedic rehab
back and neck pain
acupuncture
women's health inside
take info from our website, but also I can upload brochures from Rehab Guild NZ, take the best out of each of those and combine with our web info to provide description for each.

And on back all contact detail and QR code for our website

Target Market(s)

mostly 40 to 60 comfortably off, educated, active, some sporty, healthy, middle class

Industry/Entity Type

Education

Requirements
Must have
• Must match our website with the logo and pictures on home page
brochure to be A4 trifold DLE, please match our font or use one we can use easily
Nice to have
• not too busy, give our customers good reasons to use our services,

```html
<!DOCTYPE html>
<html lang="en">
<head>
<meta charset="utf-8">
<title>Harwick Physiotherapy – Brochure Cover</title>
<link href="https://fonts.googleapis.com/css2?family=Ubuntu:wght@400;500;700&display=swap" rel="stylesheet">
<style>
  :root {
    --orange: #e08a35;
    --orange-deep: #d4792a;
    --charcoal: #4e5358;
    --paper: #f0ede7;
    --stage: #e6e6e4;
    --white: #ffffff;
    --sky: #f3f2ee;
    --haze: #e9e5dc;
    --glow: #f2c88a;
    --dusk: #b98a56;
    --ground: #6e4c2c;
  }
  * { box-sizing: border-box; margin: 0; padding: 0; }
  html, body {
    width: 1200px; height: 800px; overflow: hidden;
    background: var(--stage);
    font-family: "Ubuntu", Arial, sans-serif;
  }
  .brochure-cover {
    position: absolute; left: 338px; top: 30px;
    width: 524px; height: 740px;
    background: var(--paper);
    box-shadow: 0 6px 24px rgba(0,0,0,.18);
    overflow: hidden;
  }
  .tagline-band {
    position: absolute; left: 0; top: 0; width: 100%; height: 92px;
    background: var(--orange);
    padding: 18px 26px;
    color: var(--white); font-size: 19px; font-weight: 500; line-height: 1.3;
  }
  .hero-photo {
    position: absolute; left: 0; top: 92px; width: 100%; height: 348px;
    background:
      radial-gradient(ellipse 70% 22% at 22% 88%, rgba(242,200,138,.95) 0%, rgba(242,200,138,0) 100%),
      linear-gradient(180deg, var(--sky) 0%, var(--haze) 62%, var(--glow) 80%, var(--dusk) 90%, var(--ground) 100%);
  }
  .headline-band {
    position: absolute; left: 0; top: 410px; width: 100%; height: 130px;
  }
  .headline-band svg { position: absolute; inset: 0; }
  .headline {
    position: absolute; left: 28px; top: 466px;
    font-size: 40px; font-weight: 400; line-height: 1.1;
    color: var(--white); letter-spacing: -.5px;
  }
  .headline strong { color: var(--charcoal); font-weight: 500; }
  .service-list {
    position: absolute; left: 322px; top: 556px;
    list-style: none; font-size: 12px; color: var(--charcoal); line-height: 1.6;
  }
  .service-list li::before { content: "•"; margin-right: 8px; }
  .brand-mark {
    position: absolute; left: 0; top: 610px; width: 38px; height: 40px;
    background: var(--orange); border-radius: 0 8px 8px 0;
  }
  .brand-name {
    position: absolute; left: 56px; top: 570px;
    font-size: 38px; font-weight: 500; line-height: 1; color: var(--charcoal);
    letter-spacing: -.5px;
  }
  .contact-details {
    position: absolute; left: 56px; top: 684px;
    font-size: 11px; font-style: normal; color: var(--charcoal); line-height: 1.5;
  }
  .website {
    position: absolute; right: 30px; top: 660px;
    font-size: 13px; color: var(--charcoal);
  }
  .edge-trim { position: absolute; left: 0; bottom: 6px; width: 100%; height: 8px; }
</style>
</head>
<body>
  <article class="brochure-cover">
    <header class="tagline-band">Providing effective, friendly, patient-centered and holistic treatment for pain and injury</header>

    <div class="hero-photo" role="img" aria-label="Photo of a woman stretching her arms overhead outdoors at sunset"></div>

    <div class="headline-band">
      <svg width="524" height="130" viewBox="0 0 524 130" aria-hidden="true">
        <polygon points="0,46 350,46 395,8 524,8 524,130 0,130" fill="var(--orange)"/>
        <polygon points="0,120 524,120 524,130 0,130" fill="var(--orange-deep)"/>
        <polygon points="458,-18 480,-18 444,40 422,40" fill="var(--charcoal)"/>
      </svg>
    </div>
    <h1 class="headline">Movement <strong>For life</strong></h1>

    <ul class="service-list">
      <li>Sports Injuries</li>
      <li>Back , neck and joint pain</li>
      <li>Orthopedic rehabilitation</li>
      <li>Acupuncture</li>
      <li>Pelvic floor Physiotherapy</li>
    </ul>

    <div class="brand-mark" aria-hidden="true"></div>
    <div class="brand-name">harwick<br>physiotherapy</div>

    <div class="website">www.harwickphysio.co.nz</div>
    <address class="contact-details">
      Carrow House, 14 Carrow Ave, Harwick<br>
      Tel.: 09 555 0142 | E-mail: info@harwickphysio.co.nz
    </address>

    <svg class="edge-trim" viewBox="0 0 524 8" preserveAspectRatio="none" aria-hidden="true">
      <polyline fill="none" stroke="#9a9a98" stroke-width="1.2"
        points="0,6 4,2 8,6 12,2 16,6 20,2 24,6 28,2 32,6 36,2 40,6 44,2 48,6 52,2 56,6 60,2 64,6 68,2 72,6 76,2 80,6 84,2 88,6 92,2 96,6 100,2 104,6 108,2 112,6 116,2 120,6 124,2 128,6 132,2 136,6 140,2 144,6 148,2 152,6 156,2 160,6 164,2 168,6 172,2 176,6 180,2 184,6 188,2 192,6 196,2 200,6 204,2 208,6 212,2 216,6 220,2 224,6 228,2 232,6 236,2 240,6 244,2 248,6 252,2 256,6 260,2 264,6 268,2 272,6 276,2 280,6 284,2 288,6 292,2 296,6 300,2 304,6 308,2 312,6 316,2 320,6 324,2 328,6 332,2 336,6 340,2 344,6 348,2 352,6 356,2 360,6 364,2 368,6 372,2 376,6 380,2 384,6 388,2 392,6 396,2 400,6 404,2 408,6 412,2 416,6 420,2 424,6 428,2 432,6 436,2 440,6 444,2 448,6 452,2 456,6 460,2 464,6 468,2 472,6 476,2 480,6 484,2 488,6 492,2 496,6 500,2 504,6 508,2 512,6 516,2 520,6 524,2"/>
    </svg>
  </article>
</body>
</html>
```